Business Card Design

After a corporate career in the finance sector I am now operating on my own as a consultant. I require a simple design, and want a strong card which is targeted at a conservative audience.

Target Market(s)

highly educated senior management, directors of companies, finance sector

Industry/Entity Type

Conservative

Contact Information for Business Card

Rosa Tindell
Consultant
Mobile: 0417 862 254
Email: rosa.tind@mailvora.com

Requirements
Should not have
• I don't want the colours green/yellow/brown

```html
<!DOCTYPE html>
<html lang="en">
<head>
<meta charset="utf-8">
<title>Rosa Tindell – Business Card</title>
<link rel="stylesheet" href="https://fonts.googleapis.com/css2?family=Maven+Pro:wght@400;500&display=swap">
<style>
  :root {
    --teal-deep: #2da594;
    --teal-bright: #55f6e4;
    --ink-white: #ffffff;
    --name-shadow: rgba(20, 110, 100, 0.55);
  }
  html, body {
    margin: 0;
    padding: 0;
    width: 1200px;
    height: 741px;
    overflow: hidden;
    background: var(--teal-bright);
  }
  .card {
    position: relative;
    width: 1200px;
    height: 741px;
    background: var(--teal-bright);
    font-family: "Maven Pro", sans-serif;
    color: var(--ink-white);
    overflow: hidden;
  }
  .band {
    position: absolute;
    left: 0;
    width: 100%;
    background: var(--teal-deep);
  }
  .band--top { top: 0; height: 82px; }
  .band--contact { top: 552px; height: 118px; }

  .identity {
    position: absolute;
    left: 0;
    width: 1210px;
    text-align: center;
  }
  .identity__name {
    position: absolute;
    top: 190px;
    left: 0;
    width: 100%;
    margin: 0;
    font-size: 112px;
    font-weight: 400;
    line-height: 1;
    letter-spacing: 0.02em;
    text-transform: uppercase;
    text-shadow: 4px 6px 6px var(--name-shadow);
  }
  .identity__role {
    position: absolute;
    top: 312px;
    left: 0;
    width: 100%;
    margin: 0;
    font-size: 33px;
    font-weight: 400;
    line-height: 1;
    letter-spacing: 0.12em;
    text-transform: uppercase;
  }

  .contact {
    position: absolute;
    top: 562px;
    left: 510px;
    margin: 0;
    font-size: 34px;
    font-weight: 400;
    line-height: 45px;
  }
  .contact__row { display: flex; }
  .contact__label { display: inline-block; }
  .contact__row--mobile .contact__label { width: 147px; }
  .contact__row--email .contact__label { width: 153px; }
</style>
</head>
<body>
  <main class="card">
    <div class="band band--top"></div>

    <header class="identity">
      <h1 class="identity__name">Rosa Tindell</h1>
      <p class="identity__role">Consultant</p>
    </header>

    <div class="band band--contact"></div>

    <address class="contact" style="font-style: normal;">
      <div class="contact__row contact__row--mobile">
        <span class="contact__label">mobile</span>
        <span class="contact__value">0417 862 254</span>
      </div>
      <div class="contact__row contact__row--email">
        <span class="contact__label">email</span>
        <span class="contact__value">rosa.tind@mailvora.com</span>
      </div>
    </address>
  </main>
</body>
</html>
```